Business Cards used to invite people to our church

We are a church and have need of a business card sized advertisement that allows our members to hand them out in order to invite people to the church. I need the front of the card to say "You're Invited" or "Come Check us out". with the service times on the back of the card later.
I have attached one of the OLD cards we have used in the past, but we want a complete makeover, into a more modern style that does not require the image.
I am also replacing the old logo with a newer "flat" logo which is attached.
Please use marketing colors. (blue or red or something that catches attention)
Create a card that DOES NOT have the picture of the two people on the front
The information on the sample card back is correct to go onto new card
Target Market(s)
anyone
Industry/Entity Type
Business
Contact Information for Business Card
sertice times and address information which you can get from the sample card I uploaded. It should have "You're Invited" or "Come Check us out" on the front of the card with out logo.

```html
<!DOCTYPE html>
<html lang="en">
<head>
<meta charset="utf-8">
<title>Harbor Light – Invitation Cards</title>
<link href="https://fonts.googleapis.com/css2?family=Dancing+Script:wght@500&family=Jost:wght@400;500;600&display=swap" rel="stylesheet">
<style>
  :root {
    --stage: #141414;
    --blue-deep: #0a50ff;
    --blue-bright: #0a7dff;
    --cyan-glow: #00f0ff;
    --blue-light: #3d9fe4;
    --blue-sea: #0b86d2;
    --panel: rgba(0, 120, 200, 0.55);
    --white: #ffffff;
  }
  * { box-sizing: border-box; margin: 0; padding: 0; }
  html, body { width: 981px; height: 1200px; overflow: hidden; background: var(--stage); }
  .canvas { position: relative; width: 981px; height: 1200px; }
  .card {
    position: absolute; left: 75px; width: 831px; height: 486px; overflow: hidden;
    font-family: "Jost", sans-serif; color: var(--white);
  }
  .card--front { top: 75px; }
  .card--back { top: 638px; }
  .card__bg { position: absolute; inset: 0; width: 100%; height: 100%; }

  .front__band {
    position: absolute; left: 0; top: 198px; width: 100%; height: 92px;
    background: linear-gradient(90deg, rgba(255,255,255,0.9) 0%, rgba(255,255,255,0.25) 8%, rgba(255,255,255,0.2) 50%, rgba(255,255,255,0.45) 92%, rgba(255,255,255,0.95) 100%);
  }
  .front__headline {
    position: absolute; left: 0; top: 198px; width: 100%; height: 92px;
    display: flex; align-items: center; justify-content: center;
    font-family: "Dancing Script", cursive; font-weight: 500; font-size: 66px;
    padding-left: 18px; letter-spacing: 0.5px;
  }

  .back__panel {
    position: absolute; left: 50px; top: 50px; width: 730px; height: 385px;
    border-radius: 16px; background: var(--panel);
  }
  .back__contact {
    position: absolute; left: 0; top: 78px; width: 100%;
    text-align: center; font-size: 29px; line-height: 40px; font-weight: 400;
  }
  .back__band {
    position: absolute; left: 0; top: 235px; width: 100%; height: 17px;
    background: linear-gradient(90deg, rgba(255,255,255,0.5), rgba(255,255,255,0.15) 50%, rgba(255,255,255,0.55));
  }
  .back__hours { position: absolute; left: 85px; top: 324px; width: 464px; font-size: 20px; line-height: 28px; }
  .hours__row { display: flex; align-items: baseline; }
  .hours__leader { flex: 1; border-bottom: 2px dotted var(--white); margin: 0 2px 5px; }
  .back__brand {
    position: absolute; left: 612px; top: 346px; display: flex; align-items: center; gap: 8px;
    font-size: 22px; font-weight: 600; letter-spacing: 1px;
  }
  .brand__mark { width: 14px; height: 14px; background: var(--white); }
</style>
</head>
<body>
<main class="canvas">
  <section class="card card--front" aria-label="Card front">
    <svg class="card__bg" viewBox="0 0 831 486" aria-hidden="true">
      <defs>
        <linearGradient id="frontRight" x1="0" y1="0" x2="1" y2="1">
          <stop offset="0" stop-color="#2a8fe8"/>
          <stop offset="0.6" stop-color="#4aa8e4"/>
          <stop offset="1" stop-color="#0586d4"/>
        </linearGradient>
        <radialGradient id="frontGlow" cx="230" cy="140" r="420" gradientUnits="userSpaceOnUse">
          <stop offset="0" stop-color="#00f4ff"/>
          <stop offset="0.35" stop-color="#00a8ff"/>
          <stop offset="1" stop-color="#0a4cff"/>
        </radialGradient>
      </defs>
      <rect width="831" height="486" fill="url(#frontRight)"/>
      <path d="M0 0 H555 C 610 190, 530 380, 300 486 H0 Z" fill="url(#frontGlow)"/>
    </svg>
    <div class="front__band"></div>
    <h1 class="front__headline">Come Check us out</h1>
  </section>

  <section class="card card--back" aria-label="Card back">
    <svg class="card__bg" viewBox="0 0 831 486" aria-hidden="true">
      <defs>
        <linearGradient id="backRight" x1="0" y1="0" x2="1" y2="1">
          <stop offset="0" stop-color="#2a8fe8"/>
          <stop offset="0.6" stop-color="#4aa8e4"/>
          <stop offset="1" stop-color="#0586d4"/>
        </linearGradient>
        <radialGradient id="backGlow" cx="170" cy="0" r="520" gradientUnits="userSpaceOnUse">
          <stop offset="0" stop-color="#00c8ff"/>
          <stop offset="0.5" stop-color="#0a7cff"/>
          <stop offset="1" stop-color="#0a4cff"/>
        </radialGradient>
      </defs>
      <rect width="831" height="486" fill="url(#backRight)"/>
      <path d="M0 0 H555 C 610 190, 530 380, 300 486 H0 Z" fill="url(#backGlow)"/>
    </svg>
    <div class="back__panel"></div>
    <address class="back__contact" style="font-style:normal">
      HARBORLIGHTCHURCH.ORG<br>
      2480 W. CEDAR LANE-MAPLETON, TX 75900<br>
      1-800-555-0142
    </address>
    <div class="back__band"></div>
    <div class="back__hours">
      <div class="hours__row"><span>SUNDAY</span><span class="hours__leader"></span><span>9:00 AM</span></div>
      <div class="hours__row"><span>SUNDAY</span><span class="hours__leader"></span><span>11:00 AM</span></div>
      <div class="hours__row"><span>Wed. Bible Class</span><span class="hours__leader"></span><span>7:00 PM</span></div>
    </div>
    <div class="back__brand"><span class="brand__mark"></span><span>HARBOR LIGHT</span></div>
  </section>
</main>
</body>
</html>
```